Upcoming lecture sponsored by a church on an important topic

We have a Reformation The Speech coming up at the end of October on the topic of law and gospel. I thought it might be cool to use a flyer that looks like it was from that day and age. Picture what Conrad Velmer would advertise things on kind of an old church/reformation type format. It will be sponsored by our church, and we have a paragraph or two to describe the lecture that would be included on the flyer. We would also want it formatted so that it could be printed on postcards and mailed to churches and individuals.

The flyer should have the following paragraph...

The distinction between the law and the gospel is the most important distinction in the Christian faith. Conrad Velmer: “Distinguishing between the law and the gospel is the highest art in Christendom, one who every person who values the name Christian ought to recognize, know, and possess.” The distinction between the law and the gospel is of great comfort for the child of God. “For the law was given by Moses, but grace and truth came by Jesus Christ” (John 1:17). For these reasons, the distinction between the law and the gospel is the most heavily assaulted doctrine in the Christian faith. This Reformation Day, join us for an explanation and defense of the great distinction between God’s good law and God’s glorious gospel.

And the flyer should have the following information...

Topic: The Steady Word and the Bright Promise
Date and Time: Tuesday, October 31, 2023 at 7:30pm
Host: Harrow Creek Fellowship Church
Speaker: Rev. Gerald Voskuil
Venue: The Marlow Hall, 5172 Brenton Avenue, Hudsonville, MI 49318
Format: Lecture followed by Q&A and refreshments

00AB8E
00BBA5
67D7C9
C6EFE9
E9F9F6

• The color scheme that I would like to have is a teal color (the same color as found at www.brackenhollowchapel.com

```html
<!DOCTYPE html>
<html lang="en">
<head>
<meta charset="utf-8">
<title>Reformation – The Speech</title>
<link href="https://fonts.googleapis.com/css2?family=Anton&family=Bebas+Neue&family=Oswald:wght@500;600&family=Pathway+Gothic+One&display=swap" rel="stylesheet">
<style>
  :root {
    --ink: #02545a;
    --paper: #f2e9d8;
    --paper-edge: #e6dac2;
    --portrait: #0b4e52;
  }
  html, body {
    margin: 0;
    padding: 0;
    width: 927px;
    height: 1200px;
    overflow: hidden;
    background: var(--paper);
  }
  .flyer {
    position: relative;
    width: 927px;
    height: 1200px;
    background: radial-gradient(ellipse at 50% 45%, #f5eedf 0%, var(--paper) 55%, var(--paper-edge) 100%);
    color: var(--ink);
    text-align: center;
    overflow: hidden;
  }
  .series {
    position: absolute;
    top: 70px; left: 0; right: 0;
    margin: 0;
    font: 600 40px/1 "Oswald", sans-serif;
    letter-spacing: 0.5px;
    text-transform: uppercase;
  }
  .host {
    position: absolute;
    top: 142px; left: 0; right: 0;
    margin: 0;
    font: 400 27px/1 "Bebas Neue", sans-serif;
    letter-spacing: 7px;
    text-transform: uppercase;
  }
  .portrait {
    position: absolute;
    top: 217px; left: 423px;
    width: 82px; height: 115px;
    background: radial-gradient(ellipse at 55% 40%, #1d6266 0%, var(--portrait) 70%);
    border-radius: 45% 45% 20% 20%;
  }
  .title {
    position: absolute;
    top: 358px; left: 0; right: 0;
    margin: 0;
    font: 400 104px/108px "Anton", sans-serif;
    letter-spacing: 2px;
    text-transform: uppercase;
  }
  .rule {
    position: absolute;
    left: 80px; width: 766px;
    height: 1.5px;
    background: var(--ink);
  }
  .rule--a { top: 585px; }
  .rule--b { top: 719px; }
  .rule--c { top: 1020px; }
  .when {
    position: absolute;
    top: 612px; left: 0; right: 0;
    margin: 0;
    font: 600 40px/1 "Oswald", sans-serif;
    text-transform: uppercase;
    transform: scaleX(0.86);
  }
  .where {
    position: absolute;
    top: 672px; left: 0; right: 0;
    margin: 0;
    font: 600 18px/1 "Oswald", sans-serif;
    text-transform: uppercase;
    transform: scaleX(0.86);
  }
  .summary {
    position: absolute;
    top: 734px; left: 88px; width: 751px;
    margin: 0;
    font: 400 19.5px/21.6px "Pathway Gothic One", sans-serif;
    text-transform: uppercase;
    letter-spacing: 0.6px;
  }
  .speaker {
    position: absolute;
    top: 1046px; left: 0; right: 0;
    margin: 0;
    font: 600 44px/1 "Oswald", sans-serif;
    text-transform: uppercase;
    transform: scaleX(0.86);
  }
  .format {
    position: absolute;
    top: 1097px; left: 0; right: 0;
    margin: 0;
    font: 400 24px/1 "Bebas Neue", sans-serif;
    letter-spacing: 3px;
    text-transform: uppercase;
  }
</style>
</head>
<body>
  <main class="flyer">
    <h2 class="series">Reformation - The Speech</h2>
    <p class="host">Harrow Creek Fellowship Church</p>
    <div class="portrait" role="img" aria-label="Small profile portrait of Conrad Velmer in teal ink"></div>
    <h1 class="title">The Steady Word and<br>the Bright Promise</h1>
    <div class="rule rule--a"></div>
    <p class="when">Tuesday, October 31, 2023 at 7:30pm</p>
    <p class="where">The Marlow Hall, 5172 Brenton Avenue, Hudsonville, MI 49318</p>
    <div class="rule rule--b"></div>
    <p class="summary">The distinction between the law and the gospel is the most important distinction in the Christian faith. Conrad Velmer: “Distinguishing between the law and the gospel is the highest art in Christendom, one who every person who values the name Christian ought to recognize, know, and possess.” The distinction between the law and the gospel is of great comfort for the child of God. “For the law was given by Moses, but grace and truth came by Jesus Christ” (John 1:17). For these reasons, the distinction between the law and the gospel is the most heavily assaulted doctrine in the Christian faith. This Reformation Day, join us for an explanation and defense of the great distinction between God’s good law and God’s glorious gospel.</p>
    <div class="rule rule--c"></div>
    <p class="speaker">Speaker: Rev. Gerald Voskuil</p>
    <p class="format">Lecture followed by Q&amp;A and refreshments</p>
  </main>
</body>
</html>
```